Velmira Body Oil Label for 4 -8 oz bottles

We are selling 4 and 8 oz body oils and need a label to put on our bottles. I'm not sure if we want a label for the front and also the back of the bottle or just one label in the front. You can give me examples of each way. Attached is our logo on a blue background but the background will change colors depending on the scent as specified in the design description. Our bottle will be either clear or white with a pump spray type lid as shown in the attached example. Attached are also our design criteria which is needed for the labels.
Updates

We have decided to use the disc top cap and not the pump spray cap. If you are able to, please show us the design on the 4 oz bottle with the disc top cap. Thanks

Target Market(s)

women

Industry/Entity Type

skincare, cosmetics

Font styles to use
Serif
Sans Serif

Requirements
Must have
• stylish name for each scented oil which contrasts the font in the logo. Also must have darker colors since the logo colors are lighter.
Nice to have
• Border around the labels, maybe one solid color or maybe two complimenting colors which go well with the fragrnace name
Should not have
• background colors that match the logo colors

```html
<!DOCTYPE html>
<html lang="en">
<head>
<meta charset="utf-8">
<title>Velmira Body Oil Labels</title>
<link rel="stylesheet" href="https://fonts.googleapis.com/css2?family=Montserrat:wght@300;600&family=Playfair+Display:wght@400;900&display=swap">
<style>
  :root {
    --page-bg: #f1f1f1;
    --white: #ffffff;
    --label-w: 200px;
    --label-h: 480px;
  }
  * { box-sizing: border-box; margin: 0; padding: 0; }
  html, body { width: 1200px; height: 675px; overflow: hidden; }
  body {
    background: radial-gradient(ellipse at center, #ffffff 0%, var(--page-bg) 80%);
    font-family: "Montserrat", sans-serif;
  }
  .label-row {
    position: absolute;
    top: 97px;
    left: 110px;
    display: flex;
    gap: 60px;
  }
  .label {
    position: relative;
    width: var(--label-w);
    height: var(--label-h);
    border-radius: 14px;
    overflow: hidden;
    color: var(--white);
    background: linear-gradient(90deg,
      var(--sheen) 0%, var(--base) 25%, var(--base) 45%,
      var(--sheen) 75%, var(--base) 100%);
  }
  .label--cotton   { --base: #fb8ba0; --sheen: #fdbfcd; --curve-a: #bfe3ff; --curve-b: #8fd1ff; --accent: #72c3f0; }
  .label--lavender { --base: #ab6ac8; --sheen: #d4abe1; --curve-a: #e4d0ee; --curve-b: #dcc2e8; --accent: #c9a3dc; }
  .label--wildwood { --base: #283a17; --sheen: #8b9b7e; --curve-a: #c5d7a0; --curve-b: #b3c98a; --accent: #a5bf6e; }
  .label--fruity   { --base: #ff9b37; --sheen: #ffc88c; --curve-a: #ffe0bf; --curve-b: #fdc996; --accent: #ffb469; }

  .label__curve { position: absolute; inset: 0; width: 100%; height: 100%; }
  .label__curve .curve-shape { fill: var(--curve-b); }

  .brand {
    position: absolute;
    top: 92px;
    left: 0; right: 0;
    display: flex;
    align-items: center;
    justify-content: center;
    gap: 8px;
    font-family: "Playfair Display", serif;
    font-weight: 400;
    font-size: 30px;
    letter-spacing: 1px;
  }
  .brand__dot { width: 9px; height: 9px; border-radius: 50%; background: var(--white); }

  .scent-name {
    position: absolute;
    left: 0; right: 0;
    text-align: center;
    font-family: "Playfair Display", serif;
    font-weight: 900;
    font-size: 42px;
    line-height: 0.95;
    letter-spacing: -1.5px;
  }
  .scent-name--two-line { top: 198px; }
  .scent-name--one-line { top: 224px; }

  .product-type {
    position: absolute;
    left: 31px;
    width: 138px;
    height: 20px;
    background: var(--white);
    color: var(--accent);
    text-align: center;
    font-weight: 300;
    font-size: 17px;
    line-height: 20px;
  }
  .product-type--low { top: 302px; }
  .product-type--high { top: 287px; }

  .claims {
    position: absolute;
    top: 370px;
    left: 0; right: 0;
    text-align: center;
    font-weight: 600;
    font-size: 9.5px;
    letter-spacing: 0.2px;
  }
  .claims__row {
    display: inline-flex;
    align-items: stretch;
    gap: 4px;
    padding-bottom: 3px;
    border-bottom: 1px solid var(--white);
  }
  .claims__divider { width: 1.5px; background: var(--white); }
  .claims__main { margin-top: 6px; }

  .volume {
    position: absolute;
    top: 444px;
    left: 0; right: 0;
    text-align: center;
    font-weight: 300;
    font-size: 9px;
  }
</style>
</head>
<body>
<main class="label-row">

  <article class="label label--cotton">
    <svg class="label__curve" viewBox="0 0 200 480" preserveAspectRatio="none" aria-hidden="true">
      <path class="curve-shape" d="M0,205 C95,172 182,265 196,470 L200,480 L0,480 Z"/>
    </svg>
    <div class="brand"><span class="brand__dot"></span>Velmira</div>
    <h2 class="scent-name scent-name--two-line">Cotton<br>Candy</h2>
    <p class="product-type product-type--low">BODY OIL</p>
    <div class="claims">
      <div class="claims__row"><span>NON-GREESY</span><span class="claims__divider"></span><span>WITH VITAMIN E</span></div>
      <p class="claims__main">ULTRA MOISTURIZING</p>
    </div>
    <p class="volume">4OZ</p>
  </article>

  <article class="label label--lavender">
    <svg class="label__curve" viewBox="0 0 200 480" preserveAspectRatio="none" aria-hidden="true">
      <path class="curve-shape" d="M0,205 C95,172 182,265 196,470 L200,480 L0,480 Z"/>
    </svg>
    <div class="brand"><span class="brand__dot"></span>Velmira</div>
    <h2 class="scent-name scent-name--two-line">Soft<br>Lavender</h2>
    <p class="product-type product-type--low">BODY OIL</p>
    <div class="claims">
      <div class="claims__row"><span>NON-GREESY</span><span class="claims__divider"></span><span>WITH VITAMIN E</span></div>
      <p class="claims__main">ULTRA MOISTURIZING</p>
    </div>
    <p class="volume">4OZ</p>
  </article>

  <article class="label label--wildwood">
    <svg class="label__curve" viewBox="0 0 200 480" preserveAspectRatio="none" aria-hidden="true">
      <path class="curve-shape" d="M0,205 C95,172 182,265 196,470 L200,480 L0,480 Z"/>
    </svg>
    <div class="brand"><span class="brand__dot"></span>Velmira</div>
    <h2 class="scent-name scent-name--one-line">Wildwood</h2>
    <p class="product-type product-type--high">BODY OIL</p>
    <div class="claims">
      <div class="claims__row"><span>NON-GREESY</span><span class="claims__divider"></span><span>WITH VITAMIN E</span></div>
      <p class="claims__main">ULTRA MOISTURIZING</p>
    </div>
    <p class="volume">4OZ</p>
  </article>

  <article class="label label--fruity">
    <svg class="label__curve" viewBox="0 0 200 480" preserveAspectRatio="none" aria-hidden="true">
      <path class="curve-shape" d="M0,205 C95,172 182,265 196,470 L200,480 L0,480 Z"/>
    </svg>
    <div class="brand"><span class="brand__dot"></span>Velmira</div>
    <h2 class="scent-name scent-name--two-line">Fruity<br>Delights</h2>
    <p class="product-type product-type--low">BODY OIL</p>
    <div class="claims">
      <div class="claims__row"><span>NON-GREESY</span><span class="claims__divider"></span><span>WITH VITAMIN E</span></div>
      <p class="claims__main">ULTRA MOISTURIZING</p>
    </div>
    <p class="volume">4OZ</p>
  </article>

</main>
</body>
</html>
```